Need posters that inspire entrepreneurs

I want to create beautiful, inspiring wall art. I'm looking for a designer to create an awesome sample (note this sample is not for real use). The winning design will form the foundation of our art "style" so there will be LOTS of ongoing work for the winning designer.

It's your challenge to create a style that is clean, inspiring and timeless, and possibly can be adapted to different colour palettes.

Looking for a perfect execution of words, image and design.

The attached example shows one idea. It should serve as an idea only.

Format of the images should be either rectangular or square. Exact size is preferably UK A4 (US letter) or max A3. Assume that a display would consist of a 4 x 4 image grid so size needs to allow for that in a small to medium size office.

The quotes I want in the 3 samples (each in an individual poster - not combined in 1 poster). Each quote should have it's own, the reason for three is to prove the design work on more than one quote. The quotes are:

1) Failure is the condiment that gives success its flavor.
– Dorian Welsby

2) Whether you think you can or think you can’t, you’re right.
– Oswald Pike

3) Ever tried. Ever failed. No matter. Try Again. Fail again. Fail better.
– Lionel Marwick

Each design should include the image of the person and the quote + any design elements you consider relevant. You should find relevant images of the individuals being quoted. The final images will not be published or used commercially in any way.

Font styles to use
Serif
Sans Serif

Colors

Designer to choose colors to be used in the design.

Requirements
Must have
• Words and headshot image - 1 per poster design.
• Please consider in the design that there will not always be photographs of the person quoted and as such the design will need to hold, whether the source is a photo, sketch or something else.
Nice to have
• None, but note that the final image will be printed on a wall mounted board, printed to the edge but not on the edge. The board will have black or white edges so consider in the design.
Should not have
• None

```html
<!DOCTYPE html>
<html lang="en">
<head>
<meta charset="utf-8">
<title>Inspiration Poster Series</title>
<link href="https://fonts.googleapis.com/css2?family=Roboto:wght@500;700;900&display=swap" rel="stylesheet">
<style>
  :root {
    --canvas: #ffffff;
    --ink-light: #ffffff;
    --ink-dark: #111111;
    --outline: #1e150d;
    --wood-light: #b89a7c;
    --wood-mid: #8f7258;
    --wood-dark: #5e4633;
    --leaf: #6aa832;
    --dust-dark: #3a2c22;
    --dust-mid: #8a6a4a;
    --dust-glow: #f2c46a;
    --sky-top: #6f7fb8;
    --sky-mid: #c4a9d6;
    --sky-warm: #fbe7a0;
    --sky-low: #f6cf5a;
    --box: #ebe3df;
    --frame: #ffffff;
    --headshot-a: #9a8a7c;
    --headshot-b: #5f5248;
  }
  * { margin: 0; padding: 0; box-sizing: border-box; }
  html, body {
    width: 1200px;
    height: 546px;
    overflow: hidden;
    background: var(--canvas);
  }
  .poster-row {
    position: relative;
    width: 1200px;
    height: 546px;
    font-family: "Roboto", Arial, sans-serif;
  }
  .poster {
    position: absolute;
    top: 46px;
    width: 334px;
    height: 454px;
    overflow: hidden;
  }
  .poster--stump { left: 54px; }
  .poster--medal { left: 432px; }
  .poster--flight { left: 810px; }

  .poster__photo {
    position: absolute;
    inset: 0;
  }
  .poster--stump .poster__photo {
    background:
      radial-gradient(circle at 58% 64%, var(--leaf) 0, rgba(106,168,50,0.55) 11%, transparent 24%),
      radial-gradient(circle at 60% 62%, var(--wood-mid) 0, var(--wood-light) 55%, var(--wood-dark) 115%);
  }
  .poster--medal .poster__photo {
    background:
      radial-gradient(circle at 74% 42%, var(--dust-glow) 0, rgba(242,196,106,0.6) 16%, transparent 42%),
      linear-gradient(160deg, var(--dust-dark) 0%, var(--dust-mid) 45%, #c79a5c 75%, var(--dust-dark) 100%);
  }
  .poster--flight .poster__photo {
    background:
      linear-gradient(90deg, transparent 62%, var(--box) 62%) bottom / 100% 40% no-repeat,
      linear-gradient(180deg, var(--sky-top) 0%, var(--sky-mid) 28%, var(--sky-warm) 62%, var(--sky-low) 100%);
  }

  .quote {
    position: absolute;
    left: 22px;
    top: 44px;
    color: var(--ink-light);
    font-weight: 700;
    white-space: nowrap;
    letter-spacing: -0.3px;
    text-shadow:
      1.5px 0 0 var(--outline), -1.5px 0 0 var(--outline),
      0 1.5px 0 var(--outline), 0 -1.5px 0 var(--outline),
      1px 1px 0 var(--outline), -1px -1px 0 var(--outline),
      1px -1px 0 var(--outline), -1px 1px 0 var(--outline);
  }
  .poster--stump .quote { left: 26px; }
  .quote__line {
    display: block;
    font-size: 23px;
    line-height: 30px;
  }
  .quote__key {
    font-size: 37px;
    font-weight: 900;
    line-height: 30px;
  }
  .quote__author {
    display: block;
    margin-top: 22px;
    font-size: 15px;
    font-weight: 700;
  }
  .poster--medal .quote__key {
    display: block;
    line-height: 36px;
  }
  .poster--medal .quote__author { margin-top: 24px; }

  .quote--dark {
    top: 97px;
    left: 20px;
    color: var(--ink-dark);
    text-shadow: none;
  }
  .quote--dark .quote__line {
    font-size: 26px;
    font-weight: 700;
    line-height: 33px;
  }
  .quote--dark .quote__author {
    margin-top: 26px;
    font-size: 15px;
  }

  .headshot {
    position: absolute;
    left: 22px;
    bottom: 22px;
    width: 62px;
    height: 62px;
    border-radius: 50%;
    border: 3px solid var(--frame);
    background: radial-gradient(circle at 50% 40%, var(--headshot-a) 0, var(--headshot-b) 100%);
  }
  .poster--stump .headshot { left: 26px; }
  .poster--flight .headshot { left: 20px; }
</style>
</head>
<body>
<main class="poster-row">
  <article class="poster poster--stump">
    <div class="poster__photo" role="img" aria-label="Photograph of a green seedling growing from a cracked tree stump"></div>
    <p class="quote">
      <span class="quote__line"><span class="quote__key">Failure</span> is the condiment</span>
      <span class="quote__line">that gives <span class="quote__key">success</span></span>
      <span class="quote__line">its flavor.</span>
      <span class="quote__author">– Dorian Welsby</span>
    </p>
    <div class="headshot" role="img" aria-label="Headshot portrait of Dorian Welsby"></div>
  </article>

  <article class="poster poster--medal">
    <div class="poster__photo" role="img" aria-label="Photograph of muddy hands raising a gold medal against a glowing dusty sky"></div>
    <p class="quote">
      <span class="quote__key">Whether</span>
      <span class="quote__line">you think you can</span>
      <span class="quote__line">or think you can’t,</span>
      <span class="quote__key">you’re</span>
      <span class="quote__line">right.</span>
      <span class="quote__author">– Oswald Pike</span>
    </p>
    <div class="headshot" role="img" aria-label="Headshot portrait of Oswald Pike"></div>
  </article>

  <article class="poster poster--flight">
    <div class="poster__photo" role="img" aria-label="Photograph of a child with cardboard wings and goggles sitting on a box, looking at a plane trail in a sunset sky"></div>
    <p class="quote quote--dark">
      <span class="quote__line">Ever tried.</span>
      <span class="quote__line">Ever failed.</span>
      <span class="quote__line">No matter.</span>
      <span class="quote__line">Try Again.</span>
      <span class="quote__line">Fail again.</span>
      <span class="quote__line">Fail better.</span>
      <span class="quote__author">– Lionel Marwick</span>
    </p>
    <div class="headshot" role="img" aria-label="Headshot portrait of Lionel Marwick"></div>
  </article>
</main>
</body>
</html>
```